Single Page Digital Brochure

We are a Sydney based finance company. We lend money to developers. Please see attached example of what we are looking to have produced. We just need a design which can be posted on LINKEDIN

Target Market(s)

Property Developers who are borrowing money

Industry/Entity Type

Finance

Requirements
Must have
• Australian relevant imagery.

TEXT TO INCLUDE:

New Offering from Ferngate Lending
Nice to have
• Design and colour scheme based around our logo (attached)

Please include the same text as the attachment

Please make the design based loosely on the attachment. But do not copy the attachement
Should not have
• Remove Text: 'Settle in under four days'

```html
<!DOCTYPE html>
<html lang="en">
<head>
<meta charset="utf-8">
<title>Ferngate Lending – New Offering</title>
<link href="https://fonts.googleapis.com/css2?family=Barlow:ital,wght@0,200;0,400;0,600;0,700;1,600&display=swap" rel="stylesheet">
<style>
  :root{
    --mat:#bcbcbc;
    --green:#234634;
    --ink:#1c1f1d;
    --white:#ffffff;
    --sky-top:#3fa9d4;
    --sky-mid:#a9d8e6;
    --sky-warm:#f2dc8c;
    --sunset:#f0b23a;
    --city:#2d3b3a;
    --water:#5fa6c4;
    --panel:rgba(255,255,255,0.42);
  }
  *{margin:0;padding:0;box-sizing:border-box}
  html,body{width:1200px;height:816px;overflow:hidden;background:var(--mat)}
  body{font-family:"Barlow",Arial,sans-serif;color:var(--ink);position:relative}
  .ad{position:absolute;left:64px;top:104px;width:1072px;height:602px;background:var(--white);overflow:hidden}
  .hero{position:absolute;left:0;top:0;width:1072px;height:488px;
    background:
      linear-gradient(180deg,rgba(0,0,0,0) 68%,var(--city) 78%,var(--city) 87%,var(--water) 89%,#8fc3d6 100%),
      linear-gradient(180deg,var(--sky-top) 0%,var(--sky-mid) 32%,#e9ecc8 50%,var(--sky-warm) 62%,var(--sunset) 74%);}
  .headline{position:absolute;left:40px;top:34px;width:420px;color:var(--green);line-height:1}
  .headline .bold{display:block;font-weight:700;font-size:58px;letter-spacing:-0.5px}
  .headline .thin{display:block;font-weight:200;font-size:54px;letter-spacing:28px;margin:4px 0 6px}
  .tagline{position:absolute;left:478px;top:42px;font-size:42px;font-weight:600;font-style:italic;color:var(--green);letter-spacing:-0.5px}
  .terms{position:absolute;left:474px;top:103px;width:572px;height:130px;background:var(--panel);
    display:grid;grid-template-columns:220px 1fr;grid-auto-rows:30.6px;padding:10px 0 0 14px;font-size:17px;color:var(--ink)}
  .terms div{white-space:nowrap}
  .terms dt{display:inline;font-weight:600;margin-right:8px}
  .terms dd{display:inline;font-weight:400}
  .contact{position:absolute;left:48px;top:514px;font-size:26px;font-weight:400;line-height:34px;color:var(--ink)}
  .contact .phone{font-weight:700;color:var(--green)}
  .brand{position:absolute;right:48px;top:520px;display:flex;flex-direction:column;align-items:center;gap:10px}
  .brand-dot{width:34px;height:34px;border-radius:50%;background:var(--green)}
  .brand-name{font-size:21px;font-weight:600;letter-spacing:1.5px;text-transform:uppercase;color:var(--green)}
</style>
</head>
<body>
  <main class="ad">
    <div class="hero" role="img" aria-label="Sunset photograph of Sydney Harbour with the Opera House, Harbour Bridge and city skyline"></div>

    <h1 class="headline">
      <span class="bold">NEW OFFERING</span>
      <span class="thin">FROM</span>
      <span class="bold">FERNGATE</span>
      <span class="bold">LENDING</span>
    </h1>

    <p class="tagline">We did. Just last week.</p>

    <dl class="terms">
      <div><dt>Loan Amount:</dt><dd>$750,000</dd></div>
      <div><dt>Repayments:</dt><dd>Capitalized</dd></div>
      <div><dt>Rate:</dt><dd>7.79%</dd></div>
      <div><dt>Turnaround:</dt><dd>Settled in 4 days</dd></div>
      <div><dt>Term</dt><dd>12 months</dd></div>
      <div><dt>Security:</dt><dd>2x Sydney Residential Properties</dd></div>
      <div><dt>LVR:</dt><dd>60%</dd></div>
      <div><dt>Purpose:</dt><dd>Business Working Capital</dd></div>
    </dl>

    <p class="contact">Call Mara today on <span class="phone">0400 555 219</span> or<br>mara@ferngatelending.com</p>

    <div class="brand">
      <span class="brand-dot"></span>
      <span class="brand-name">Ferngate Lending</span>
    </div>
  </main>
</body>
</html>
```